Create a responsive clean and mean platform

We support global forensic investigations (like trellmark or corvath files). We help the clients (Chief Legal Officer) to get insights on potential risks to their company and how to act on them. When in need they will immediately call us. we want to create a platform that supports the client in everydaty tasks considering forensic and risks.

Homepage (after login client): This page has following areas:
There should be a standard layout on every page with search, messages, navigation and login name (you see the client is logged in)

1. first area shows different risk and issues related to the company using the platform. There are different types of alerts and issues, like, compliance issues, risk issues, risk alerts, industry alerts and business alerts. You are able to click on the alerts and go into more details. The area of issues gives the option for view between list details or an icon view.
Second area on this page: It's big and show a map in the style provided (see screenshots). The map show an overview of new articles from around the world. The news article related to the client business are plotted on the map. Every time there is a new news feed, you will have a small pop up that shows the feed for 2 seconds top right corner. The map is interactive and also has a timeline in the bottom to slide from a year ago to now.
Third area: Shows a process status of a silver kite project. It shows the complete process and the current status.
Fourth area: Shows two overviews of budget Vs. Costs and Planned Vs. Actual. When clicking on them the client goes to a page with more detail.

Search page: We would like a search page that shows the search results of for example Corvath files. It contains two different areas. First showing are issues and risk from within the company that are related to "Corvath files". With a short description on the issue and that the issue was resolved a week ago. '
Second area: contains news related articles, with header, small picture related to "corvath files".

Issue Detail Page: Contains details about the issues and alerts you clicked from the homepage. The details contains to call to action parts: one is to navigate to get in contact for this particular issue. The second part is related document. Apart from that you also see other related issues and alerts.

Get in contact for certain issue/alert page:
Contains contact cards as shown in the style examples. On the left you first see contact card with the title Head Quarter. Contact: Maudie Ferlow with a picture of the contact. Like in the screenshot, except you can push a call button or email button.
Below another contact card in the same style with Regional. Contact: Cedric Hollaway and also you can push a call button or email button.
On the right side you see current subscription that says three things: Prevent, Detect and Repond full platinum subscription
Below just like in the example you see three experts with name photo and expertise.

Any other colors then what we included. Icons and stuff and cool graphics are always welcome.
Please use the screenshots provided as reference for the design style.

Target Market(s)

Client Chief Officer (CLO)

Industry/Entity Type

Security

Number of Pages Required

4 page

Font styles to use
Other font styles liked:
• If possible frutiger or open sans if not Sans serif

Colors
9bcb3c
0555a3
0592cd

Requirements
Must have
• It should be a clean and sterile platform. Which is light from color and uses color to accentuate risk issue's and call to action.
• Please use the following color codes: Dark blue R0 G39 B118, Green R129 G188 B0, blue R0 G161 B222, Light blue R114 G199 B231, Dark green R60 G138 B46, light green R189 G210 B3.
Nice to have
• next to desktop also one page on zuvo
Should not have
• It's a side from business to business. So don't be loosley in use of drawn graphics. Icons are welcome ofcourse

```html
<!DOCTYPE html>
<html lang="en">
<head>
<meta charset="utf-8">
<title>Vestral Forensics – Client Dashboard</title>
<link rel="stylesheet" href="https://fonts.googleapis.com/css2?family=Lato:wght@400;700&family=Open+Sans:wght@400;600;700&display=swap">
<style>
:root{
  --blue:#0555a3;
  --blue-dark:#002776;
  --blue-band:#0a55a4;
  --cyan:#0592cd;
  --green:#9bcb3c;
  --green-soft:#c6e48a;
  --ink:#1d1d1d;
  --text:#333a40;
  --line:#d9dde2;
  --panel:rgba(255,255,255,.88);
  --footer:#202224;
  --amber:#f2b21e;
  --amber-dark:#c98a08;
  --amber-edge:#b07506;
  --teal:#12b9d2;
  --teal-dark:#0a7f91;
}
*{box-sizing:border-box;margin:0;padding:0}
html,body{width:1200px;height:2582px;overflow:hidden}
body{
  position:relative;
  font-family:"Lato",sans-serif;
  color:var(--text);
  background:
    radial-gradient(ellipse 700px 500px at 90% 8%,rgba(130,170,240,.45),transparent 70%),
    radial-gradient(ellipse 600px 400px at 10% 15%,rgba(120,200,235,.35),transparent 70%),
    radial-gradient(ellipse 800px 300px at 50% 2380px,rgba(190,225,130,.45),transparent 70%),
    radial-gradient(ellipse 600px 250px at 5% 2250px,rgba(120,190,235,.35),transparent 70%),
    linear-gradient(#e6f1fb 0,#f3f9ff 700px,#ffffff 880px,#ffffff 2000px,#eef6fb 2200px,#f1f8e6 2530px);
}
h2{font-weight:400}
.abs{position:absolute}

/* header */
.site-header{left:0;top:0;width:1200px;height:86px;background:rgba(255,255,255,.45);border-bottom:1px solid rgba(255,255,255,.8)}
.brand{left:81px;top:22px;display:flex;align-items:center;gap:14px}
.brand-dot{width:40px;height:40px;border-radius:50%;background:var(--blue)}
.brand-name{font-family:"Open Sans",sans-serif;font-size:34px;font-weight:400;color:var(--blue);letter-spacing:.5px}
.toolbar{left:836px;top:14px;display:flex;align-items:center;gap:14px}
.tool{width:32px;height:32px;position:relative;display:flex;align-items:center;justify-content:center}
.tool-badge{position:absolute;right:-2px;top:-2px;width:15px;height:15px;border-radius:50%;background:var(--green);color:#111;font-size:10px;font-weight:700;display:flex;align-items:center;justify-content:center}
.user-chip{width:112px;height:47px;background:var(--blue);display:flex;align-items:center;gap:8px;padding-left:9px;margin-left:6px}
.user-photo{width:31px;height:31px;border:2px solid #fff;background:linear-gradient(#8aa3bd,#4d6b8c)}
.user-name{color:#fff;font-family:"Open Sans",sans-serif;font-size:18px}

/* cards */
.card{background:var(--panel);box-shadow:0 1px 3px rgba(0,0,0,.12)}
.card-head{height:52px;background:var(--blue);display:flex;align-items:center;gap:10px;padding-left:24px;color:#fff;font-family:"Open Sans",sans-serif;font-size:22px;font-weight:400}
.card-head.small{height:47px;padding-left:12px}
.head-icon{position:relative;width:32px;height:30px;display:flex;align-items:center;justify-content:center}
.head-badge{position:absolute;left:12px;top:-4px;width:17px;height:17px;border-radius:50%;background:var(--green);color:#111;font-size:11px;font-weight:700;display:flex;align-items:center;justify-content:center}
.issue-list{list-style:none;padding:10px 18px 0 26px}
.issue-list li{display:flex;gap:12px;padding:11px 0 10px;border-bottom:1px solid var(--line);font-size:13.5px;line-height:20px;color:#222}
.issue-list li:last-child{border-bottom:none}
.issue-list.alerts{padding:16px 14px 0 14px}
.issue-list.alerts li{padding:5px 0 28px 0;margin-bottom:4px}
.bullet{flex:0 0 16px;height:16px;margin-top:2px}

/* map band */
.map-band{left:0;top:885px;width:1200px;height:580px;background:var(--blue-band)}
.band-title{left:0;top:22px;width:1200px;text-align:center;color:#fff;font-family:"Open Sans",sans-serif;font-size:31px;font-weight:400}
.world-map{left:215px;top:88px;width:741px;height:404px;border-radius:40px;background:radial-gradient(ellipse at 50% 45%,#0d1c33 0,#102444 55%,rgba(10,85,164,0) 78%)}
.pin{width:20px;height:28px}
.news-tip{left:417px;top:327px;width:149px;height:48px;background:#fff;border:1px solid #999;font-size:11.5px;font-weight:700;color:#111;text-align:center;line-height:15px;padding-top:8px}
.news-tip::after{content:"";position:absolute;left:66px;bottom:-8px;border:8px solid transparent;border-bottom:0;border-top-color:#fff}
.timeline{left:102px;top:500px;width:967px;height:20px;border-radius:10px;background:#d6d6d6}
.timeline-thumb{left:492px;top:-8px;width:34px;height:48px;border-radius:4px;background:linear-gradient(#f4f4f4,#cfcfcf);border:1px solid #b8b8b8}
.timeline-label{left:0;top:537px;width:1212px;text-align:center;color:#fff;font-family:"Open Sans",sans-serif;font-weight:700;font-size:17px}

/* process */
.section-title{left:0;top:1480px;width:1200px;text-align:center;font-family:"Open Sans",sans-serif;font-size:34px;font-weight:400;color:var(--ink)}
.section-title span{color:var(--blue)}
.process-panel{left:296px;top:1537px;width:608px;height:551px;background:rgba(245,247,248,.8)}

/* charts */
.chart-card{top:2161px;height:311px}
.chart-body{position:relative;height:259px}
.legend{left:410px;top:95px;display:flex;flex-direction:column;gap:11px}
.legend span{width:67px;height:28px;color:#fff;font-size:12px;display:flex;align-items:center;justify-content:center}
.legend .budget{background:var(--blue)}
.legend .costs{background:var(--green)}

/* footer */
.site-footer{left:0;top:2533px;width:1200px;height:49px;background:var(--footer);color:#e8e8e8;font-size:14px}
.copyright{left:81px;top:15px}
.social{left:955px;top:9px;display:flex;gap:12px}
.social i{width:32px;height:32px;border-radius:50%;border:2px solid #fff;display:block}
</style>
</head>
<body>

<header class="site-header abs">
  <div class="brand abs"><span class="brand-dot"></span><span class="brand-name">VESTRAL FORENSICS</span></div>
  <nav class="toolbar abs" aria-label="Main">
    <span class="tool" aria-label="Home"><svg width="28" height="26" viewBox="0 0 28 26"><path d="M14 2 1 14h4v11h7v-7h4v7h7V14h4z" fill="#222"/></svg></span>
    <span class="tool" aria-label="Messages"><svg width="24" height="26" viewBox="0 0 24 26"><path d="M12 2c-5 0-7 4-7 8v6l-3 4h20l-3-4v-6c0-4-2-8-7-8zM9 22a3 3 0 0 0 6 0z" fill="#222"/></svg><span class="tool-badge">2</span></span>
    <span class="tool" aria-label="Call"><svg width="28" height="28" viewBox="0 0 28 28"><path d="M4 10c0-4 4-6 10-6s10 2 10 6l-5 2-1-3c-2-.6-6-.6-8 0l-1 3zM8 14h12l3 10H5z" fill="#222"/><circle cx="14" cy="19" r="3" fill="#fff"/></svg></span>
    <span class="tool" aria-label="Search"><svg width="26" height="26" viewBox="0 0 26 26"><circle cx="10" cy="10" r="7" fill="none" stroke="#222" stroke-width="3"/><path d="m15 15 8 8" stroke="#222" stroke-width="3.5" stroke-linecap="round"/></svg></span>
    <span class="user-chip"><span class="user-photo" role="img" aria-label="Profile photo"></span><span class="user-name">JOHN</span></span>
  </nav>
</header>

<svg width="0" height="0" class="abs">
  <symbol id="chev" viewBox="0 0 16 16"><circle cx="8" cy="8" r="6.5" fill="none" stroke="#222" stroke-width="1.6"/><path d="m6.5 5 3 3-3 3" fill="none" stroke="#222" stroke-width="1.8"/></symbol>
  <symbol id="pin" viewBox="0 0 20 28"><path d="M10 0a9 9 0 0 0-9 9c0 7 9 19 9 19s9-12 9-19a9 9 0 0 0-9-9z" fill="#9bcb3c"/><circle cx="10" cy="9" r="3.5" fill="#0a55a4"/></symbol>
</svg>

<!-- issues -->
<section class="card abs" style="left:124px;top:127px;width:441px;height:312px">
  <h2 class="card-head"><span class="head-icon"><svg width="26" height="30" viewBox="0 0 26 30"><rect x="3" y="2" width="18" height="25" fill="none" stroke="#111" stroke-width="2"/><path d="M7 8h10M7 13h10M7 18h7" stroke="#111" stroke-width="2"/></svg></span>Compliance Issues</h2>
  <ul class="issue-list">
    <li><svg class="bullet"><use href="#chev"/></svg><span>Lorem ipsum dolor sit amet, consectetuer adipiscing elit, sed diam nonummy nibh euismod tincidunt ut laoreet dolore magna aliquam erat volutpat.</span></li>
    <li><svg class="bullet"><use href="#chev"/></svg><span>Lorem ipsum dolor sit amet, consectetuer adipiscing elit, sed diam nonummy nibh euismod tincidunt ut laoreet dolore magna aliquam erat volutpat.</span></li>
    <li><svg class="bullet"><use href="#chev"/></svg><span>Lorem ipsum dolor sit amet, consectetuer adipiscing elit, sed diam nonummy nibh euismod tincidunt ut laoreet dolore magna aliquam erat volutpat.</span></li>
  </ul>
</section>

<section class="card abs" style="left:622px;top:127px;width:441px;height:312px">
  <h2 class="card-head"><span class="head-icon" style="width:52px"><svg width="52" height="24" viewBox="0 0 52 24"><path d="M2 20 14 8l10 9L38 4l12 10" fill="none" stroke="#111" stroke-width="2"/><circle cx="14" cy="8" r="2.5" fill="#111"/><circle cx="24" cy="17" r="2.5" fill="#111"/><circle cx="38" cy="4" r="2.5" fill="#111"/></svg></span>Risk Issues</h2>
  <ul class="issue-list">
    <li><svg class="bullet"><use href="#chev"/></svg><span>Lorem ipsum dolor sit amet, consectetuer adipiscing elit, sed diam nonummy nibh euismod tincidunt ut laoreet dolore magna aliquam erat volutpat.</span></li>
    <li><svg class="bullet"><use href="#chev"/></svg><span>Lorem ipsum dolor sit amet, consectetuer adipiscing elit, sed diam nonummy nibh euismod tincidunt ut laoreet dolore magna aliquam erat volutpat.</span></li>
    <li><svg class="bullet"><use href="#chev"/></svg><span>Lorem ipsum dolor sit amet, consectetuer adipiscing elit, sed diam nonummy nibh euismod tincidunt ut laoreet dolore magna aliquam erat volutpat.</span></li>
  </ul>
</section>

<!-- alerts -->
<section class="card abs" style="left:79px;top:487px;width:329px;height:336px">
  <h2 class="card-head small"><span class="head-icon"><svg width="28" height="28" viewBox="0 0 28 28"><circle cx="12" cy="16" r="9" fill="none" stroke="#111" stroke-width="2.5"/><path d="M12 11v6" stroke="#111" stroke-width="2.5"/></svg><span class="head-badge">5</span></span>Risk Alerts</h2>
  <ul class="issue-list alerts">
    <li><svg class="bullet"><use href="#chev"/></svg><span>Lorem ipsum dolor sit amet, consectetuer adipiscing elit, sed diam nonummy nibh euismod tincidunt ut.</span></li>
    <li><svg class="bullet"><use href="#chev"/></svg><span>Lorem ipsum dolor sit amet, consectetuer adipiscing elit, sed diam nonummy nibh euismod tincidunt ut.</span></li>
    <li><svg class="bullet"><use href="#chev"/></svg><span>Lorem ipsum dolor sit amet, consectetuer adipiscing elit, sed diam nonummy nibh euismod tincidunt ut.</span></li>
  </ul>
</section>

<section class="card abs" style="left:436px;top:487px;width:327px;height:345px">
  <h2 class="card-head small"><span class="head-icon"><svg width="30" height="26" viewBox="0 0 30 26"><path d="M2 24V12l7-4v4l7-4v4l7-4v16zM24 24V4h4v20z" fill="#111"/></svg><span class="head-badge">5</span></span>Industry Alerts</h2>
  <ul class="issue-list alerts">
    <li><svg class="bullet"><use href="#chev"/></svg><span>Lorem ipsum dolor sit amet, consectetuer adipiscing elit, sed diam nonummy nibh euismod tincidunt ut.</span></li>
    <li><svg class="bullet"><use href="#chev"/></svg><span>Lorem ipsum dolor sit amet, consectetuer adipiscing elit, sed diam nonummy nibh euismod tincidunt ut.</span></li>
    <li><svg class="bullet"><use href="#chev"/></svg><span>Lorem ipsum dolor sit amet, consectetuer adipiscing elit, sed diam nonummy nibh euismod tincidunt ut.</span></li>
  </ul>
</section>

<section class="card abs" style="left:790px;top:487px;width:329px;height:336px">
  <h2 class="card-head small"><span class="head-icon"><svg width="30" height="28" viewBox="0 0 30 28"><circle cx="12" cy="16" r="7" fill="none" stroke="#111" stroke-width="4" stroke-dasharray="3 2.5"/><circle cx="23" cy="8" r="4" fill="none" stroke="#111" stroke-width="3" stroke-dasharray="2 2"/></svg><span class="head-badge">5</span></span>Business Alerts</h2>
  <ul class="issue-list alerts">
    <li><svg class="bullet"><use href="#chev"/></svg><span>Lorem ipsum dolor sit amet, consectetuer adipiscing elit, sed diam nonummy nibh euismod tincidunt ut.</span></li>
    <li><svg class="bullet"><use href="#chev"/></svg><span>Lorem ipsum dolor sit amet, consectetuer adipiscing elit, sed diam nonummy nibh euismod tincidunt ut.</span></li>
    <li><svg class="bullet"><use href="#chev"/></svg><span>Lorem ipsum dolor sit amet, consectetuer adipiscing elit, sed diam nonummy nibh euismod tincidunt ut.</span></li>
  </ul>
</section>

<!-- news map -->
<section class="map-band abs">
  <h2 class="band-title abs">Overview of New Articles From Around The World</h2>
  <div class="world-map abs" role="img" aria-label="World map with dark continents showing news article locations"></div>
  <svg class="pin abs" style="left:338px;top:180px"><use href="#pin"/></svg>
  <svg class="pin abs" style="left:484px;top:157px"><use href="#pin"/></svg>
  <svg class="pin abs" style="left:410px;top:250px"><use href="#pin"/></svg>
  <svg class="pin abs" style="left:298px;top:316px"><use href="#pin"/></svg>
  <svg class="pin abs" style="left:534px;top:388px"><use href="#pin"/></svg>
  <svg class="pin abs" style="left:624px;top:260px"><use href="#pin"/></svg>
  <svg class="pin abs" style="left:741px;top:171px"><use href="#pin"/></svg>
  <svg class="pin abs" style="left:775px;top:235px"><use href="#pin"/></svg>
  <svg class="pin abs" style="left:928px;top:143px"><use href="#pin"/></svg>
  <div class="news-tip abs">Lorem ipsum dolor sit<br>amet, almet consect</div>
  <div class="timeline abs"><span class="timeline-thumb abs"></span></div>
  <div class="timeline-label abs">Year 2000</div>
</section>

<!-- process -->
<h2 class="section-title abs">Our <span>Process</span></h2>
<section class="process-panel abs" aria-label="Project process status">
  <svg width="608" height="551" viewBox="0 0 608 551">
    <circle cx="320" cy="228" r="203" fill="none" stroke="#bfe07a" stroke-width="2"/>
    <circle cx="320" cy="228" r="197" fill="none" stroke="#bfe07a" stroke-width="2"/>
    <circle cx="320" cy="228" r="155" fill="none" stroke="#eaf3d8" stroke-width="26"/>
    <circle cx="320" cy="228" r="46" fill="var(--green)"/>
    <path d="M320 380v150" stroke="#b5d95e" stroke-width="3" stroke-dasharray="14 10"/>
  </svg>
</section>

<!-- budget chart -->
<section class="card chart-card abs" style="left:124px;width:441px">
  <h2 class="card-head" style="padding-left:40px">Budget Vs. Costs</h2>
  <div class="chart-body">
    <svg class="abs" style="left:20px;top:20px" width="380" height="230" viewBox="0 0 380 230">
      <g stroke="#e3e3e3" stroke-width="1">
        <path d="M38 10h330M38 31h330M38 52h330M38 73h330M38 94h330M38 115h330M38 136h330M38 157h330M38 178h330M38 199h330"/>
        <path d="M38 10v189M65 10v189M92 10v189M119 10v189M146 10v189M173 10v189M200 10v189M227 10v189M254 10v189M281 10v189M308 10v189M335 10v189"/>
      </g>
      <g font-size="10" fill="#333" text-anchor="end" font-family="Lato,sans-serif">
        <text x="30" y="24">900</text><text x="30" y="45">800</text><text x="30" y="66">700</text><text x="30" y="87">600</text><text x="30" y="108">500</text><text x="30" y="129">400</text><text x="30" y="150">300</text><text x="30" y="171">200</text><text x="30" y="192">100</text><text x="30" y="203">0</text>
      </g>
      <g fill="var(--blue)">
        <rect x="48" y="94" width="4" height="105"/><rect x="75" y="119" width="4" height="80"/><rect x="102" y="138" width="4" height="61"/><rect x="129" y="31" width="4" height="168"/><rect x="156" y="94" width="4" height="105"/><rect x="183" y="119" width="4" height="80"/><rect x="210" y="138" width="4" height="61"/><rect x="237" y="119" width="4" height="80"/><rect x="264" y="94" width="4" height="105"/><rect x="291" y="69" width="4" height="130"/><rect x="318" y="41" width="4" height="158"/><rect x="345" y="10" width="4" height="189"/>
      </g>
      <g fill="var(--green)">
        <rect x="53" y="136" width="4" height="63"/><rect x="80" y="149" width="4" height="50"/><rect x="107" y="151" width="4" height="48"/><rect x="134" y="94" width="4" height="105"/><rect x="161" y="136" width="4" height="63"/><rect x="188" y="149" width="4" height="50"/><rect x="215" y="151" width="4" height="48"/><rect x="242" y="149" width="4" height="50"/><rect x="269" y="136" width="4" height="63"/><rect x="296" y="119" width="4" height="80"/><rect x="323" y="102" width="4" height="97"/><rect x="350" y="81" width="4" height="118"/>
      </g>
      <g font-size="9" fill="#333" text-anchor="middle" font-family="Lato,sans-serif">
        <text x="52" y="215">Jan</text><text x="79" y="215">Feb</text><text x="106" y="215">Mar</text><text x="133" y="215">Apr</text><text x="160" y="215">May</text><text x="187" y="215">Jun</text><text x="214" y="215">Jul</text><text x="241" y="215">Aug</text><text x="268" y="215">Sep</text><text x="295" y="215">Oct</text><text x="322" y="215">Nov</text><text x="349" y="215">Dec</text>
      </g>
    </svg>
    <div class="legend abs"><span class="budget">Budget</span><span class="costs">Costs</span></div>
  </div>
</section>

<!-- planned chart -->
<section class="card chart-card abs" style="left:622px;width:441px">
  <h2 class="card-head" style="padding-left:32px">Planned Vs. Actual</h2>
  <div class="chart-body">
    <svg class="abs" style="left:40px;top:8px" width="360" height="240" viewBox="0 0 360 240" role="img" aria-label="Pie chart: 96 percent planned, 4 percent actual">
      <!-- large slice: side walls -->
      <path d="M295 115A125 75 0 0 1 45 115L45 149A125 75 0 0 0 295 149Z" fill="var(--amber-dark)"/>
      <path d="M170 115L191.7 41.1L191.7 75.1L170 149Z" fill="var(--amber-edge)"/>
      <!-- large slice: top -->
      <path d="M170 115L287.5 89.3A125 75 0 1 1 191.7 41.1Z" fill="var(--amber)"/>
      <!-- small slice, pulled out -->
      <path d="M202 101L319.5 75.3L319.5 109.3L202 135Z" fill="var(--teal-dark)"/>
      <path d="M202 101L223.7 27.1A125 75 0 0 1 319.5 75.3Z" fill="var(--teal)"/>
      <g font-family="Open Sans,sans-serif" font-weight="700" fill="#fff">
        <text x="75" y="135" font-size="18">96 %</text>
        <text x="236" y="70" font-size="16">04 %</text>
      </g>
    </svg>
  </div>
</section>

<footer class="site-footer abs">
  <p class="copyright abs">Copyright 2016 © VESTRAL FORENSICS .&nbsp;&nbsp; All Rights Reserved</p>
  <div class="social abs" aria-label="Social links"><i></i><i></i><i></i><i></i></div>
</footer>

</body>
</html>
```